Football field themed poster-game

I'm looking for a 22" x 29" size poster with a minimum of 300dpi, max of 300mb. File format can be jpg, gif, tiff or bmp. Would like the field portion of the poster to appear like a real grass football field. The field will need makers for each yard. I've added an addition simple clip art that shows another way for yard lines as well.The rest of the layout I would like similar, but made to look more professional. Wording should be the same as in the given draft and located in the same area or close to that area on the poster. The style is open, but should be a little minimalist in nature. Design work has to be original and cannot be taken from trademarked or copyrighted items.
Updates

Project Deadline Extended
Reason: I have 2 or 3 designs that really standout, but I would like to see just a few more.

Target Market(s)

Football fans

Font styles to use
Sans Serif

Colors

Designer to choose colors to be used in the design.

Requirements
Must have
• The design must have the same similar layout as the file I have submitted with the contest. The football field needs to be made to look like a real field with turf. boarders would be nice and a modern look.
Should not have
• hard to read fonts, changes to the major overall layout of poster.

```html
<!DOCTYPE html>
<html lang="en">
<head>
<meta charset="utf-8">
<title>Kickoff Cup – Field Game Poster</title>
<link href="https://fonts.googleapis.com/css2?family=Graduate&family=Montserrat:wght@700&family=Roboto+Slab:wght@700&display=swap" rel="stylesheet">
<style>
  :root {
    --page: #ffffff;
    --visitor-red: #d12a05;
    --visitor-band: #e14816;
    --visitor-circle: #fde3e2;
    --home-blue: #1036a0;
    --home-band: #1c3ea6;
    --home-circle: #e1e5fb;
    --turf-light: #6fa33a;
    --turf-mid: #5a9030;
    --turf-dark: #4b7f27;
    --chalk: #ffffff;
  }
  * { box-sizing: border-box; margin: 0; padding: 0; }
  html, body { width: 910px; height: 1200px; overflow: hidden; background: var(--page); }
  .poster { position: relative; width: 910px; height: 1200px; background: var(--page); }

  .score-panel { position: absolute; left: 11px; width: 351px; height: 351px; }
  .score-panel svg { display: block; width: 100%; height: 100%; }
  .score-panel--visitors { top: 11px; background: var(--visitor-red); transform: rotate(180deg); }
  .score-panel--home { top: 836px; background: var(--home-blue); }
  .score-label {
    font-family: "Montserrat", sans-serif; font-weight: 700; font-size: 42px; letter-spacing: 2px;
  }

  .game-badge {
    position: absolute; left: 9px; top: 375px; width: 356px; height: 448px;
    background: radial-gradient(circle at 50% 45%, var(--turf-light), var(--turf-mid) 60%, var(--turf-dark));
    display: flex; align-items: center; justify-content: center; gap: 14px;
  }
  .game-badge__dot { width: 34px; height: 34px; border-radius: 50%; background: #f1eed8; }
  .game-badge__name {
    font-family: "Montserrat", sans-serif; font-weight: 700; font-size: 38px;
    color: #f1eed8; letter-spacing: 2px; text-transform: uppercase;
  }

  .field { position: absolute; left: 376px; top: 10px; width: 524px; height: 1177px; }
  .end-zone {
    position: absolute; left: 0; width: 524px; height: 94px;
    display: flex; align-items: center; justify-content: center;
    font-family: "Graduate", sans-serif; font-size: 64px; color: var(--chalk); letter-spacing: 1px;
  }
  .end-zone--visitors { top: 0; background: var(--visitor-band); transform: rotate(180deg); }
  .end-zone--home { bottom: 0; background: var(--home-band); }
  .turf {
    position: absolute; left: 0; top: 94px; width: 524px; height: 989px;
    background: linear-gradient(90deg, var(--turf-mid), var(--turf-light) 50%, var(--turf-mid));
  }
  .turf svg { display: block; }
  .yard-number { font-family: "Roboto Slab", sans-serif; font-weight: 700; font-size: 38px; fill: var(--chalk); }
</style>
</head>
<body>
<main class="poster">

  <section class="score-panel score-panel--visitors" aria-label="Visitors score">
    <svg viewBox="0 0 351 351">
      <circle cx="175" cy="183" r="139" fill="none" stroke="var(--chalk)" stroke-width="2"/>
      <circle cx="175" cy="183" r="134" fill="var(--visitor-circle)" stroke="var(--chalk)" stroke-width="3"/>
      <path d="M105.6 83.9 A121 121 0 0 1 244.4 83.9" fill="none" stroke="var(--chalk)" stroke-width="44"/>
      <path id="score-arc-visitors" d="M93.8 114.8 A106 106 0 0 1 256.2 114.8" fill="none"/>
      <text class="score-label" fill="var(--visitor-red)"><textPath href="#score-arc-visitors" startOffset="50%" text-anchor="middle">SCORE</textPath></text>
    </svg>
  </section>

  <section class="game-badge" role="img" aria-label="Kickoff Cup game badge on turf with a football and radiating lines">
    <span class="game-badge__dot"></span>
    <span class="game-badge__name">Kickoff Cup</span>
  </section>

  <section class="score-panel score-panel--home" aria-label="Home score">
    <svg viewBox="0 0 351 351">
      <circle cx="175" cy="183" r="139" fill="none" stroke="var(--chalk)" stroke-width="2"/>
      <circle cx="175" cy="183" r="134" fill="var(--home-circle)" stroke="var(--chalk)" stroke-width="3"/>
      <path d="M105.6 83.9 A121 121 0 0 1 244.4 83.9" fill="none" stroke="var(--chalk)" stroke-width="44"/>
      <path id="score-arc-home" d="M93.8 114.8 A106 106 0 0 1 256.2 114.8" fill="none"/>
      <text class="score-label" fill="var(--home-blue)"><textPath href="#score-arc-home" startOffset="50%" text-anchor="middle">SCORE</textPath></text>
    </svg>
  </section>

  <section class="field" aria-label="Football field">
    <div class="end-zone end-zone--visitors">VISITORS</div>
    <div class="turf">
      <svg width="524" height="989" viewBox="0 0 524 989">
        <g class="yard-lines" stroke="var(--chalk)" stroke-width="2.5">
          <line x1="0" x2="524" y1="1.5" y2="1.5"/>
          <line x1="0" x2="524" y1="49.4" y2="49.4"/>
          <line x1="0" x2="524" y1="98.8" y2="98.8"/>
          <line x1="0" x2="524" y1="148.2" y2="148.2"/>
          <line x1="0" x2="524" y1="197.6" y2="197.6"/>
          <line x1="0" x2="524" y1="247" y2="247"/>
          <line x1="0" x2="524" y1="296.4" y2="296.4"/>
          <line x1="0" x2="524" y1="345.8" y2="345.8"/>
          <line x1="0" x2="524" y1="395.2" y2="395.2"/>
          <line x1="0" x2="524" y1="444.6" y2="444.6"/>
          <line x1="0" x2="524" y1="494" y2="494"/>
          <line x1="0" x2="524" y1="543.4" y2="543.4"/>
          <line x1="0" x2="524" y1="592.8" y2="592.8"/>
          <line x1="0" x2="524" y1="642.2" y2="642.2"/>
          <line x1="0" x2="524" y1="691.6" y2="691.6"/>
          <line x1="0" x2="524" y1="741" y2="741"/>
          <line x1="0" x2="524" y1="790.4" y2="790.4"/>
          <line x1="0" x2="524" y1="839.8" y2="839.8"/>
          <line x1="0" x2="524" y1="889.2" y2="889.2"/>
          <line x1="0" x2="524" y1="938.6" y2="938.6"/>
          <line x1="0" x2="524" y1="987.5" y2="987.5"/>
        </g>
        <g class="hash-marks" stroke="var(--chalk)" stroke-width="4" stroke-dasharray="2 7.88">
          <line x1="196" x2="196" y1="10" y2="980"/>
          <line x1="325" x2="325" y1="10" y2="980"/>
        </g>
        <g class="yard-numbers yard-numbers--left">
          <text class="yard-number" text-anchor="middle" transform="translate(91 98.8) rotate(90)" dy="13">10</text>
          <text class="yard-number" text-anchor="middle" transform="translate(91 197.6) rotate(90)" dy="13">20</text>
          <text class="yard-number" text-anchor="middle" transform="translate(91 296.4) rotate(90)" dy="13">30</text>
          <text class="yard-number" text-anchor="middle" transform="translate(91 395.2) rotate(90)" dy="13">40</text>
          <text class="yard-number" text-anchor="middle" transform="translate(91 494) rotate(90)" dy="13">50</text>
          <text class="yard-number" text-anchor="middle" transform="translate(91 592.8) rotate(90)" dy="13">40</text>
          <text class="yard-number" text-anchor="middle" transform="translate(91 691.6) rotate(90)" dy="13">30</text>
          <text class="yard-number" text-anchor="middle" transform="translate(91 790.4) rotate(90)" dy="13">20</text>
          <text class="yard-number" text-anchor="middle" transform="translate(91 889.2) rotate(90)" dy="13">10</text>
        </g>
        <g class="yard-numbers yard-numbers--right">
          <text class="yard-number" text-anchor="middle" transform="translate(426 98.8) rotate(-90)" dy="13">10</text>
          <text class="yard-number" text-anchor="middle" transform="translate(426 197.6) rotate(-90)" dy="13">20</text>
          <text class="yard-number" text-anchor="middle" transform="translate(426 296.4) rotate(-90)" dy="13">30</text>
          <text class="yard-number" text-anchor="middle" transform="translate(426 395.2) rotate(-90)" dy="13">40</text>
          <text class="yard-number" text-anchor="middle" transform="translate(426 494) rotate(-90)" dy="13">50</text>
          <text class="yard-number" text-anchor="middle" transform="translate(426 592.8) rotate(-90)" dy="13">40</text>
          <text class="yard-number" text-anchor="middle" transform="translate(426 691.6) rotate(-90)" dy="13">30</text>
          <text class="yard-number" text-anchor="middle" transform="translate(426 790.4) rotate(-90)" dy="13">20</text>
          <text class="yard-number" text-anchor="middle" transform="translate(426 889.2) rotate(-90)" dy="13">10</text>
        </g>
      </svg>
    </div>
    <div class="end-zone end-zone--home">HOME</div>
  </section>

</main>
</body>
</html>
```